Wordpress site needed asap for modern mobile app dev company

Hi
We are looking for someone to design a very modern looking website with company logo that outlines what our business is and let's users purchase a mobile app designed by our company. (For ideas think lumvex.io or kritobuild.com) The user should be able to describe what functionality they require and we will go and provide a test version of their app built .
The pages we would like are:
Home
Pricing (giving them an option to buy the options available)
Testimonials
Contact
I currently have hosting on PMV Hosting with wordpress installed, so if this could be taken into account that would be great. I also have square turn template if this could be incorporated.

```html
<!DOCTYPE html>
<html lang="en">
<head>
<meta charset="utf-8">
<title>NUVIO — Mobile App Developer</title>
<link href="https://fonts.googleapis.com/css2?family=Open+Sans:wght@400;600;700&family=Oswald:wght@400;500&display=swap" rel="stylesheet">
<style>
:root{
  --blue:#2ba2da;
  --blue-dark:#1d86c0;
  --navy:#1f6d97;
  --sky:#3aaee0;
  --ink:#333;
  --muted:#777;
  --line:#dcdcdc;
  --paper:#fff;
  --mist:#eef0f2;
  --charcoal:#2b2b2b;
  --teal-btn:#1c6e8e;
}
*{box-sizing:border-box;margin:0;padding:0}
html,body{width:1200px;height:2508px;overflow:hidden}
body{position:relative;background:var(--paper);font-family:"Open Sans",Arial,sans-serif;color:var(--ink)}
.abs{position:absolute}

/* header */
.site-header{left:0;top:0;width:1200px;height:120px;background:var(--paper)}
.brand{left:86px;top:34px;font-size:44px;font-weight:400;color:var(--blue);letter-spacing:2px;line-height:1.2}
.main-nav{left:500px;top:46px;display:flex;align-items:center;gap:38px;font-size:15px;font-weight:600;color:#555}
.main-nav .active{color:var(--blue)}
.nav-btn{border:2px solid var(--blue);color:var(--blue);padding:6px 16px;font-size:13px;border-radius:2px}
.nav-btn.fill{background:var(--blue);color:#fff;margin-left:-26px}

/* hero */
.hero{left:0;top:120px;width:1200px;height:600px;background:radial-gradient(ellipse at 55% 40%,#2f6d8a 0%,#14304a 40%,#080d16 80%)}
.hero-caption{left:352px;top:500px;width:488px;height:140px;background:rgba(0,0,0,.6);color:#fff;font-family:Oswald,Arial,sans-serif;padding:18px 26px;white-space:nowrap}
.hero-caption h1{font-size:42px;font-weight:500;line-height:1.15;letter-spacing:.5px}
.hero-caption p{font-size:33px;font-weight:400;line-height:1.35}
.hero-arrow{top:425px;width:14px;height:14px;border-top:3px solid #fff;border-left:3px solid #fff}
.hero-arrow.prev{left:24px;transform:rotate(-45deg)}
.hero-arrow.next{right:24px;transform:rotate(135deg)}

/* intro */
.intro{top:720px;height:260px;width:600px;color:#fff;padding:34px 88px 0}
.intro.who{left:0;background:var(--navy)}
.intro.offer{left:600px;background:var(--sky);padding-left:40px;padding-right:40px}
.intro h2{font-size:26px;font-weight:600;letter-spacing:1px;margin-bottom:12px;line-height:1.2}
.intro p{font-size:13px;line-height:1.6}
.read-more{display:inline-block;margin-top:20px;background:#fff;color:var(--ink);font-size:11px;padding:6px 14px;border-radius:2px}

/* pricing */
.pricing{left:0;top:980px;width:1200px;height:560px;background:var(--mist)}
.phone{left:100px;top:1060px;width:220px;height:440px;border-radius:34px;background:linear-gradient(160deg,#fafafa,#d9dcdf);border:2px solid #cfd2d5}
.phone-logo{left:100px;top:1262px;width:220px;text-align:center;font-size:38px;color:var(--blue);letter-spacing:2px}
.section-title{width:1200px;text-align:center;font-size:26px;font-weight:600;letter-spacing:1px;line-height:1.2}
.pricing-title{left:140px;top:1030px}
.plan{background:#fff;text-align:center;box-shadow:0 6px 16px rgba(0,0,0,.18)}
.plan-head{background:var(--blue);color:#fff;font-size:26px;font-weight:600;height:72px;line-height:72px}
.plan.featured .plan-head{background:var(--blue-dark);height:88px;line-height:88px;font-size:28px}
.price{font-size:34px;color:var(--ink);margin-top:22px}
.details{display:inline-block;background:var(--blue);color:#fff;font-size:11px;font-weight:700;padding:4px 20px;margin-top:10px}
.features{list-style:none;text-align:left;width:130px;margin:18px auto 0;font-size:11px;color:#555;line-height:2}
.features li::before{content:"✓";color:var(--ink);margin-right:6px;font-weight:700}
.purchase{position:absolute;left:20px;right:20px;bottom:26px;background:var(--blue);color:#fff;font-size:13px;font-weight:700;height:44px;line-height:44px}

/* testimonials */
.testimonials{left:0;top:1540px;width:1200px;height:400px;background:linear-gradient(180deg,#3a3a3a 0%,#262626 100%)}
.testimonials-title{left:0;top:1620px;color:#fff}
.quote{top:1712px;width:330px;display:flex;gap:18px;align-items:flex-start}
.avatar{width:96px;height:96px;border-radius:50%;background:radial-gradient(circle at 50% 40%,#c8c2b8,#6d6a66);border:3px solid #fff;flex:none}
.quote-body{color:#ddd;font-size:13px;line-height:1.5;padding-top:14px;position:relative}
.quote-body::before{content:"“";position:absolute;left:-14px;top:0;font-size:26px;color:#bbb}
.quote-name{color:var(--blue);font-size:11px;font-weight:700;margin-top:6px}
.quote-role{color:var(--blue);font-size:11px}

/* contact */
.contact-title{left:0;top:1994px;color:var(--navy)}
.contact-sub{left:0;top:2036px;width:1200px;text-align:center;font-size:14px;color:var(--muted)}
.field{height:40px;border:1px solid var(--line);background:#fff;font-size:12px;color:#666;padding:11px 12px}
.send{left:268px;top:2272px;width:664px;height:58px;background:var(--teal-btn);color:#fff;text-align:center;line-height:58px;font-size:20px;font-weight:600;letter-spacing:1px}

/* footer */
.site-footer{left:0;top:2400px;width:1200px;height:108px;background:var(--charcoal)}
.copyright{left:86px;top:2444px;color:#ccc;font-size:12px}
.social{top:2432px;width:34px;height:34px}
.to-top{left:1140px;top:2444px;color:#bbb;font-size:12px}
</style>
</head>
<body>

<header class="abs site-header"></header>
<div class="abs brand">NUVIO</div>
<nav class="abs main-nav">
  <span class="active">HOME</span>
  <span>PRICING</span>
  <span>TESTIMONIALS</span>
  <span>CONTACT US</span>
  <span class="nav-btn">LOGIN</span>
  <span class="nav-btn fill">SIGN UP</span>
</nav>

<section class="abs hero" role="img" aria-label="Two smartphones in a glowing space scene with app icons and a city skyline streaming between them"></section>
<div class="abs hero-arrow prev"></div>
<div class="abs hero-arrow next"></div>
<div class="abs hero-caption">
  <h1>MOBILE APP DEVELOPER</h1>
  <p>Small business &amp; enterprises</p>
</div>

<section class="abs intro who">
  <h2>WHO WE ARE</h2>
  <p>We build fast, clean mobile apps for small teams and growing brands. From the first sketch to launch day, our designers and developers work with you to shape ideas into apps your customers will enjoy using every day.</p>
  <span class="read-more">Read More</span>
</section>
<section class="abs intro offer">
  <h2>WHAT WE OFFER</h2>
  <p>Tell us what your app should do and we will deliver a working test version. Choose HTML5, Orbit or Pearl builds, with clear pricing, steady support and updates that keep your app running smoothly.</p>
  <span class="read-more">Read More</span>
</section>

<section class="abs pricing"></section>
<div class="abs phone" role="img" aria-label="White smartphone showing the app name on its screen"></div>
<div class="abs phone-logo">NUVIO</div>
<h2 class="abs section-title pricing-title" style="color:var(--ink)">PRICING</h2>

<div class="abs plan" style="left:395px;top:1120px;width:195px;height:370px">
  <div class="plan-head">HTML5 APP</div>
  <div class="price">$19.99</div>
  <span class="details">DETAILS</span>
  <ul class="features"><li>Responsive layout</li><li>Free test build</li><li>Email support</li></ul>
  <div class="purchase">PURCHASE</div>
</div>
<div class="abs plan featured" style="left:615px;top:1088px;width:240px;height:415px">
  <div class="plan-head">ORBIT APP</div>
  <div class="price">$39.99</div>
  <span class="details">DETAILS</span>
  <ul class="features"><li>Responsive layout</li><li>Free test build</li><li>Email support</li></ul>
  <div class="purchase" style="height:52px;line-height:52px">PURCHASE</div>
</div>
<div class="abs plan" style="left:878px;top:1120px;width:195px;height:370px">
  <div class="plan-head">PEARL APP</div>
  <div class="price">$29.99</div>
  <span class="details">DETAILS</span>
  <ul class="features"><li>Responsive layout</li><li>Free test build</li><li>Email support</li></ul>
  <div class="purchase">PURCHASE</div>
</div>

<section class="abs testimonials" role="img" aria-label="Dark backdrop of a tablet with colourful app icons"></section>
<h2 class="abs section-title testimonials-title">TESTIMONIALS</h2>

<div class="abs quote" style="left:92px">
  <div class="avatar" role="img" aria-label="Client portrait"></div>
  <div class="quote-body">Great team, quick replies and a polished app delivered right on time.
    <div class="quote-name">Daniel Reyes</div><div class="quote-role">Marketing Director</div></div>
</div>
<div class="abs quote" style="left:440px">
  <div class="avatar" role="img" aria-label="Client portrait"></div>
  <div class="quote-body">They turned our rough idea into an Orbit app our clients love.
    <div class="quote-name">Sarah Lind</div><div class="quote-role">Store Owner</div></div>
</div>
<div class="abs quote" style="left:785px">
  <div class="avatar" role="img" aria-label="Client portrait"></div>
  <div class="quote-body">Clear pricing, honest advice and a smooth launch for our Pearl app.
    <div class="quote-name">Omar Hale</div><div class="quote-role">Startup Founder</div></div>
</div>

<h2 class="abs section-title contact-title">CONTACT US</h2>
<p class="abs contact-sub">Neque porro quisquam est qui dolorem ipsum quia dolor sit amet</p>
<div class="abs field" style="left:268px;top:2080px;width:326px">First Name</div>
<div class="abs field" style="left:606px;top:2080px;width:326px">Last Name</div>
<div class="abs field" style="left:268px;top:2134px;width:326px">Phone</div>
<div class="abs field" style="left:606px;top:2134px;width:326px">Email Id</div>
<div class="abs field" style="left:268px;top:2188px;width:664px;height:58px">Message</div>
<div class="abs send">SEND</div>

<footer class="abs site-footer"></footer>
<div class="abs copyright">Copyright © 2016, All Rights Reserved</div>
<div class="abs social" style="left:955px;background:#2ba2da"></div>
<div class="abs social" style="left:995px;background:#d8412f"></div>
<div class="abs social" style="left:1035px;background:#3b5998"></div>
<div class="abs social" style="left:1075px;background:#1b75b6"></div>
<div class="abs to-top">
  <svg width="14" height="14" viewBox="0 0 14 14"><path d="M2 10 L7 4 L12 10" fill="none" stroke="#bbb" stroke-width="2"/></svg>
</div>

</body>
</html>
```